BOLD & MINIMALIST DESIGN NEEDED

We want a very bold but minimalistic business card design that is impactful and utilizes both sides of the business card. Our current logo is included for your use.

We want bold fonts and good use of negative space. We don't want the logo to overpower the design.

Target Market(s)

Professionals who are building new commercial buildings.

Industry/Entity Type

Construction

Contact Information for Business Card

Name, Title, email, office phone, cell phone, website

Font styles to use
Serif
Sans Serif

Requirements
Must have
• Bold design!

```html
<!DOCTYPE html>
<html lang="en">
<head>
<meta charset="utf-8">
<title>Ridgeline Design + Build — Business Card</title>
<link rel="stylesheet" href="https://fonts.googleapis.com/css2?family=Montserrat:wght@400;500;800&display=swap">
<style>
  :root {
    --stage: #262626;
    --ink: #0b0b0b;
    --paper: #ffffff;
    --green: #7dc42a;
    --green-soft: #a6d86a;
    --emboss: #2b2b2b;
  }
  * { margin: 0; padding: 0; box-sizing: border-box; }
  html, body { width: 1200px; height: 1015px; overflow: hidden; }
  body {
    background: var(--stage);
    font-family: "Montserrat", Arial, sans-serif;
    display: flex;
    flex-direction: column;
    align-items: center;
    justify-content: center;
    gap: 56px;
  }
  .card {
    position: relative;
    width: 640px;
    height: 366px;
    overflow: hidden;
  }

  /* Shared brand lockup: one colour, one weight */
  .brand {
    position: absolute;
    display: flex;
    align-items: center;
    gap: 14px;
  }
  .brand-square { flex: none; background: var(--green); }
  .brand-text {
    font-weight: 800;
    text-transform: uppercase;
    line-height: 1.05;
    text-align: right;
  }
  .brand-name { display: block; letter-spacing: 1px; }
  .brand-tag { display: block; letter-spacing: 6px; }

  /* Back side */
  .card-back { background: var(--ink); }
  .back-band {
    position: absolute;
    left: 0; top: 0; bottom: 0;
    width: 34px;
    background: linear-gradient(180deg, var(--green-soft), var(--green));
  }
  .card-back .brand { right: 56px; bottom: 66px; }
  .card-back .brand-square { width: 18px; height: 18px; }
  .card-back .brand-text { color: var(--emboss); }
  .card-back .brand-name { font-size: 46px; }
  .card-back .brand-tag { font-size: 16px; }

  /* Front side */
  .card-front { background: var(--paper); }
  .name-block {
    position: absolute;
    left: 0;
    top: 96px;
    display: flex;
    align-items: stretch;
  }
  .name-marker {
    width: 40px;
    background: var(--green);
    margin-right: 18px;
  }
  .person-name {
    font-weight: 800;
    font-size: 23px;
    letter-spacing: 0.5px;
    color: var(--ink);
    text-transform: uppercase;
    line-height: 1.2;
  }
  .person-title {
    font-weight: 500;
    font-size: 14px;
    color: var(--green);
    text-transform: uppercase;
    letter-spacing: 0.5px;
  }
  .card-front .brand { right: 44px; top: 62px; }
  .card-front .brand-square { width: 16px; height: 16px; }
  .card-front .brand-text { color: var(--ink); }
  .card-front .brand-name { font-size: 34px; }
  .card-front .brand-tag { font-size: 12px; letter-spacing: 5px; }

  .contact-list {
    position: absolute;
    left: 118px;
    bottom: 44px;
    list-style: none;
  }
  .contact-item {
    display: flex;
    align-items: center;
    gap: 10px;
    font-size: 17px;
    font-weight: 400;
    color: var(--ink);
    line-height: 1.55;
  }
  .contact-item svg { width: 16px; height: 16px; flex: none; }
</style>
</head>
<body>

<section class="card card-back" aria-label="Card back">
  <div class="back-band"></div>
  <div class="brand">
    <span class="brand-square"></span>
    <span class="brand-text">
      <span class="brand-name">Ridgeline</span>
      <span class="brand-tag">Design + Build</span>
    </span>
  </div>
</section>

<section class="card card-front" aria-label="Card front">
  <div class="name-block">
    <div class="name-marker"></div>
    <div>
      <p class="person-name">Marcus Hale</p>
      <p class="person-title">Managing Director</p>
    </div>
  </div>

  <div class="brand">
    <span class="brand-square"></span>
    <span class="brand-text">
      <span class="brand-name">Ridgeline</span>
      <span class="brand-tag">Design + Build</span>
    </span>
  </div>

  <ul class="contact-list">
    <li class="contact-item">
      <svg viewBox="0 0 16 16" fill="var(--green)"><path d="M3.5 1.5l2.5 0 1 3.5-1.7 1.2a8 8 0 0 0 4.5 4.5L11 9l3.5 1v2.5c0 1-1 2-2 2C6.5 14.5 1.5 9.5 1.5 3.5c0-1 1-2 2-2z"/></svg>
      044-555 010 274
    </li>
    <li class="contact-item">
      <svg viewBox="0 0 16 16" fill="none" stroke="var(--green)" stroke-width="1.6"><rect x="4" y="1" width="8" height="14" rx="1.5"/><line x1="7" y1="12.5" x2="9" y2="12.5"/></svg>
      044-555 010 391
    </li>
    <li class="contact-item">
      <svg viewBox="0 0 16 16" fill="var(--green)"><path d="M1 3h14v10H1z"/><path d="M1 3l7 6 7-6" fill="none" stroke="#fff" stroke-width="1.4"/></svg>
      info@ridgelinebuild.com
    </li>
    <li class="contact-item">
      <svg viewBox="0 0 16 16" fill="none" stroke="var(--green)" stroke-width="1.4"><circle cx="8" cy="8" r="6.5"/><ellipse cx="8" cy="8" rx="3" ry="6.5"/><line x1="1.5" y1="8" x2="14.5" y2="8"/></svg>
      www.ridgelinebuild.com
    </li>
  </ul>
</section>

</body>
</html>
```